Velvet Lantern rebranding my business with a new business card

I have my new logo and now I need a refresher on my business cards. I really want something fun and fresh. I like black background or anything to make the color pop.
Logo
Name: Velvet Lantern
Contact Info as stated below:
Mara Pelkin
519-555-0147
Logo
Name: Velvet Lantern
Mara Pelkin
519-555-0147
fb.me/VelvetLanternbyMara
Instagram: @VelvetLanternbyMara

Industry/Entity Type

Business

Contact Information for Business Card

double-sided. Logo on one side. Contact info on the other.

Requirements
Must have
• Logo
• Name: Velvet Lantern
• Contact Info as stated below:
• Mara Pelkin
• 519-555-0147
• fb.me/VelvetLanternbyMara
• fb.me/VelvetLanternbyMara

```html
<!DOCTYPE html>
<html lang="en">
<head>
<meta charset="utf-8">
<title>Velvet Lantern – Business Card</title>
<link rel="stylesheet" href="https://fonts.googleapis.com/css2?family=Noticia+Text&family=Raleway:wght@400;600&display=swap">
<style>
  :root {
    --stage: #111111;
    --card-black: #1b1b1b;
    --cream: #efe6c8;
    --red: #d8262e;
    --grey: #c9c9c9;
    --teal: #5ec9bc;
    --pink: #f0a8b4;
    --sand: #e3d2ad;
    --logo-ink: #8fd3c6;
    --logo-ink-back: #2b2b2b;
  }
  * { margin: 0; padding: 0; box-sizing: border-box; }
  html, body { width: 1200px; height: 1000px; overflow: hidden; background: var(--stage); }
  .stage { position: relative; width: 1200px; height: 1000px; }

  .card {
    position: absolute;
    width: 520px;
    height: 300px;
    border-radius: 22px;
    box-shadow: 0 12px 30px rgba(0,0,0,.55);
    overflow: hidden;
  }

  /* Front: contact side */
  .card--front { left: 60px; top: 230px; background: var(--card-black); }
  .front__brand {
    position: absolute; left: 40px; top: 110px;
    display: flex; align-items: center; gap: 12px;
    white-space: nowrap;
  }
  .brand-mark { width: 28px; height: 28px; border-radius: 50%; background: var(--logo-ink); flex: none; }
  .brand-name {
    font-family: "Raleway", sans-serif; font-weight: 600;
    font-size: 24px; color: var(--logo-ink); line-height: 1.1;
    white-space: nowrap;
  }
  .front__contact { position: absolute; right: 36px; top: 70px; text-align: right; }
  .person-name { font-family: "Noticia Text", serif; font-size: 36px; line-height: 1; white-space: nowrap; }
  .person-name .first { color: var(--cream); }
  .person-name .last { color: var(--red); }
  .phone {
    margin-top: 12px; font-family: "Raleway", sans-serif; font-size: 17px;
    color: var(--grey); letter-spacing: .5px;
  }
  .front__social { position: absolute; right: 36px; bottom: 30px; text-align: right; }
  .social-icons { display: flex; justify-content: flex-end; gap: 8px; margin-bottom: 8px; }
  .social-icon { width: 20px; height: 20px; border-radius: 50%; background: var(--cream); }
  .handle { font-family: "Raleway", sans-serif; font-size: 19px; color: var(--grey); white-space: nowrap; }
  .handle .accent { color: var(--red); }

  /* Back: logo side */
  .card--back {
    left: 620px; top: 470px;
    background: linear-gradient(135deg, var(--pink) 0%, var(--teal) 42%, var(--sand) 100%);
    display: flex; align-items: center; justify-content: center; gap: 16px;
  }
  .card--back .brand-mark { width: 40px; height: 40px; background: var(--logo-ink-back); }
  .card--back .brand-name { font-size: 40px; color: var(--logo-ink-back); }
</style>
</head>
<body>
<main class="stage">
  <section class="card card--front" aria-label="Business card, contact side">
    <div class="front__brand">
      <span class="brand-mark"></span>
      <span class="brand-name">Velvet Lantern</span>
    </div>
    <div class="front__contact">
      <p class="person-name"><span class="first">Mara</span> <span class="last">Pelkin</span></p>
      <p class="phone">519-555-0147</p>
    </div>
    <div class="front__social">
      <div class="social-icons" aria-hidden="true">
        <span class="social-icon"></span>
        <span class="social-icon"></span>
      </div>
      <p class="handle">Velvet<span class="accent">Lantern</span>by<span class="accent">Mara</span></p>
    </div>
  </section>

  <section class="card card--back" aria-label="Business card, logo side">
    <span class="brand-mark"></span>
    <span class="brand-name">Velvet Lantern</span>
  </section>
</main>
</body>
</html>
```